Our company TrulaPay, an online processor of payments is seeking talented submissions for our website redesign. The winning design will be chopped up and converted into a WordPress theme to allow for easy content additions and updates.

We are looking for modern designs that rival current websites in our industry (plimo.example, zanquetto.example, holvix.example, brandle.example, quillmarkcharges.example, evensplitcharges.example, KoboRun.example).

Our company is seeking to expand our reach to software developers and engineers who are either integrating our payment platform into their offerings or are engineering a custom solution for the company they work for and are in need of a payment platform such as our own.

We currently work with hundreds of different business partners whom either resell our services or integrate our processing capabilities into their software (which they sell). We also must communicate effectively to end users, businesses, who seek us out directly for their payment processing needs.

We are open to different color schemes but would ultimately like them to be somewhat inline with our current logo (see attached). Our website needs to instill security and confidence to any current and/or potential user as we are trusted with private and sensitive information.

We are seeking submissions from qualified; individual freelancers, freelance teams, and agencies who can attack this project in its entirety. Since this project is a total redesign, we would like submissions that have the capability to design any custom graphics, icons, buttons, and illustrations in line with our industry, capabilities, offerings, and content. We are looking for someone to design our new website and would prefer a vendor who can also help us to design elements (graphics, illustrations, charts, workflows) within our website.

Designs will be converted into a wordpress theme and we would like to utilize widgets for as many areas as possible to make editing and updating easy.

We are seeking the creation of a few unique pages but many of the pages for the majority of our content will just be internal content pages which will be duplicated.

We will likely contract with the winning submission for future work.

Please see Design Reference Document for more information

Target Market(s)

Resellers
Merchant Service Providers
Software Developers
Independent Sales Organizations (ISOs)
App Builders
Mobile App Builders
Independent Software Developers
Organizational Software Developers
Businesses who need to accept payments
Governments
Municipalities
Schools
DMVs
Courts
Retailers
Medical Offices
Hosipitals
Clinics
Dr. Offices
Gyms
Churches
Non-Profits
Software Companies
Technology Companies
Startups

• Logo cannot change drastically.

```html
<!DOCTYPE html>
<html lang="en">
<head>
<meta charset="utf-8">
<title>TrulaPay – ACH Payment Processing</title>
<link rel="stylesheet" href="https://fonts.googleapis.com/css2?family=Oswald:wght@300;400&family=Open+Sans:wght@400;600&display=swap">
<style>
:root{
  --navy:#1c2a8c;
  --ink:#222;
  --text:#3a3a3a;
  --muted:#8a8a8a;
  --rule:#d6d6d6;
  --nav-top:#a9a9a9;
  --nav-bot:#7d7d7d;
  --band:#cfcfcf;
  --footer:#343434;
  --footer-text:#ececec;
  --white:#fff;
}
*{box-sizing:border-box;margin:0;padding:0}
html,body{width:985px;height:1200px;overflow:hidden;background:var(--white)}
body{position:relative;font-family:Arial,Helvetica,sans-serif;color:var(--text)}
.abs{position:absolute}

/* header */
.brand{left:116px;top:14px;font:600 34px/1 "Open Sans",sans-serif;color:var(--navy);letter-spacing:-1px}
.contact-email{left:729px;top:16px;font:400 12px "Open Sans",sans-serif;color:#444;display:flex;align-items:center;gap:8px}
.login{left:811px;top:13px;width:58px;height:20px;border:1px solid #c5c5c5;border-radius:2px;background:linear-gradient(#f4f4f4,#dedede);font:400 12px/18px "Open Sans",sans-serif;color:#555;display:flex;align-items:center;justify-content:center;gap:4px}
.contact-phone{left:729px;top:44px;font:400 15px "Open Sans",sans-serif;color:#444;display:flex;align-items:center;gap:10px;letter-spacing:.5px}

/* nav */
.nav{left:0;top:83px;width:985px;height:32px;background:linear-gradient(var(--nav-top),var(--nav-bot));border-bottom:3px solid #eee}
.nav ul{list-style:none;position:absolute;left:116px;top:0;display:flex;height:32px}
.nav li{font:400 12px/32px "Oswald",sans-serif;color:#fff;text-align:center;border-right:1px solid #6e6e6e}
.nav li.active{background:#f4f4f4;color:#333}
.search{left:723px;top:89px;width:147px;height:21px;border-radius:10px;background:#fff;font:400 10px/21px Arial,sans-serif;color:#aaa;padding-left:9px}
.search svg{position:absolute;right:7px;top:4px}

/* hero */
.hero{top:118px;height:364px;border-bottom:3px solid #a0a0a0}
.hero-left{left:0;width:485px;background:linear-gradient(120deg,#d9dde2 0%,#b8bec6 45%,#eef0f2 100%)}
.hero-right{left:492px;width:493px;background:linear-gradient(135deg,#5b7a9d 0%,#b9c8d6 45%,#dfe6ee 100%)}
.caption{top:323px;height:112px;background:rgba(40,40,40,.72);color:#fff;padding:10px 13px}
.caption h2{font:400 23px/1.2 "Open Sans",sans-serif}
.caption p{font:600 12px/15px "Open Sans",sans-serif;margin-top:2px}
.caption-right{text-align:right}
.cta{display:inline-flex;margin-top:6px;height:28px;border-radius:3px;overflow:hidden}
.cta span{font:300 17px/28px "Oswald",sans-serif;padding:0 10px;background:#7a7a7a}
.cta i{width:28px;background:#333;display:flex;align-items:center;justify-content:center}
.caption-right .cta span{background:#4a4a4a}
.dots{left:803px;top:454px;display:flex;gap:4px}
.dots b{width:12px;height:12px;border-radius:50%;border:1px solid #fff;background:rgba(255,255,255,.2)}
.dots b.on{background:#c8c8c8}

/* section headings */
.h-title{font:400 22px/1 "Oswald",sans-serif;color:#333;display:flex;align-items:flex-end;gap:5px;padding-bottom:8px;border-bottom:2px dotted var(--rule);white-space:nowrap;letter-spacing:-.3px}
.h-title em{font-style:normal;color:var(--muted)}

.welcome{left:116px;top:506px;width:497px}
.welcome .lead{font:700 10px/15px Arial,sans-serif;color:var(--ink);margin-top:10px}
.welcome p{font-size:9.3px;line-height:15px;margin-top:7px}
.more{font:700 9.5px Arial,sans-serif;color:#444;display:flex;align-items:center;gap:5px;justify-content:flex-end}

.industries{left:630px;top:506px;width:240px}
.industries ul{list-style:none;margin-top:8px;border:1px solid #cfcfcf}
.industries li{height:25px;border-bottom:1px solid #cfcfcf;background:linear-gradient(#fafafa,#ececec);font:400 12px/25px "Open Sans",sans-serif;color:#333;padding-left:24px;position:relative}
.industries li:last-child{border-bottom:none}
.industries li::before{content:"";position:absolute;left:9px;top:9px;width:5px;height:5px;border-right:1.5px solid #aaa;border-top:1.5px solid #aaa;transform:rotate(45deg)}
.industries li.active{background:#cdcdcd}
.industries li.active::before{border-color:#333}
.industries li.active::after{content:"»";position:absolute;right:10px;top:-2px;font-size:18px;color:#444}

/* processing band */
.band{left:0;top:762px;width:985px;height:318px;background:var(--band);border-top:1px solid #bbb}
.band-title{left:0;top:780px;width:985px;text-align:center;font:400 23px "Oswald",sans-serif;color:#333}
.band-title em{font-style:normal;color:var(--muted)}
.card{top:822px;width:240px;height:228px;background:#fff;border:1px solid #bdbdbd;border-radius:3px;padding:8px}
.card .photo{height:120px;border:1px solid #ccc}
.card h3{font:400 12px "Open Sans",sans-serif;color:#333;margin:8px 2px 4px;white-space:nowrap;letter-spacing:-.2px}
.card p{font-size:9.3px;line-height:14px;margin:0 2px}
.card .more{margin-top:8px;margin-right:6px}

/* footer */
.site-footer{color:var(--footer-text)}
.footer{left:0;top:1081px;width:985px;height:119px;background:var(--footer)}
.foot-nav{left:116px;top:1092px;width:365px;font:700 9.5px Arial,sans-serif;color:#fff;padding-bottom:8px;border-bottom:1px solid #555}
.foot-nav span{margin:0 5px;color:#aaa;font-weight:400}
.addr{top:1124px;font-size:9.5px;line-height:14px;color:var(--footer-text)}
.addr b{display:block;color:#fff}
.foot-brand{left:724px;top:1094px;font:600 24px "Open Sans",sans-serif;color:#5a5a5a;letter-spacing:-1px}
.follow{left:698px;top:1147px;font:400 20px "Oswald",sans-serif;color:#fff;display:flex;align-items:center;gap:8px}
.follow i{width:24px;height:24px;border-radius:2px;display:block}
.copy{left:0;top:1180px;width:985px;text-align:center;font-size:9.5px;color:#ddd;padding-left:5px}
</style>
</head>
<body>

<header>
  <div class="abs brand">TrulaPay</div>
  <div class="abs contact-email">
    <svg width="19" height="13" viewBox="0 0 19 13"><rect x=".5" y=".5" width="18" height="12" fill="#999"/><path d="M1 1l8.5 7L18 1" stroke="#fff" fill="none"/></svg>
    Email us
  </div>
  <div class="abs login">Log in
    <svg width="9" height="11" viewBox="0 0 9 11"><rect x="0" y="5" width="9" height="6" fill="#777"/><path d="M2 5V3a2.5 2.5 0 0 1 5 0" stroke="#777" fill="none" stroke-width="1.4"/></svg>
  </div>
  <div class="abs contact-phone">
    <svg width="19" height="19" viewBox="0 0 19 19"><rect width="19" height="19" rx="2" fill="#999"/><path d="M6 4l2 3-1 1.5c1 2 2 3 3.5 3.5L12 11l3 2-1 2c-5 0-10-5-10-10z" fill="#fff"/></svg>
    555-013-4477
  </div>
</header>

<nav class="abs nav">
  <ul>
    <li class="active" style="width:66px">Home</li>
    <li style="width:86px">Solutions</li>
    <li style="width:94px">Developers</li>
    <li style="width:81px">Partners</li>
    <li style="width:86px">Company</li>
    <li style="width:88px">Resources</li>
    <li style="width:64px">Blog</li>
  </ul>
</nav>
<div class="abs search">Search
  <svg width="13" height="13" viewBox="0 0 13 13"><circle cx="5.5" cy="5.5" r="4" stroke="#888" stroke-width="1.6" fill="none"/><path d="M8.5 8.5L12 12" stroke="#888" stroke-width="1.8"/></svg>
</div>

<section>
  <div class="abs hero hero-left" role="img" aria-label="Photo of a young businessman in a suit working at a laptop in an office"></div>
  <div class="abs hero hero-right" role="img" aria-label="Close-up photo of a hand typing on a laptop keyboard"></div>
  <div class="abs caption" style="left:116px;width:317px">
    <h2>Businesses</h2>
    <p>Lorem ipsum dolor sit amet cons adipisicing elit, sed do eiusm Duis aute irure.</p>
    <div class="cta"><span>Click Here</span><i><svg width="16" height="16" viewBox="0 0 16 16"><circle cx="8" cy="8" r="8" fill="#fff"/><path d="M6 4.5l5 3.5-5 3.5z" fill="#333"/></svg></i></div>
  </div>
  <div class="abs caption caption-right" style="left:551px;width:318px">
    <h2>Developers</h2>
    <p>Lorem ipsum dolor sit amet cons adipisicing elit, sed do eiusm Duis aute irure.</p>
    <div class="cta"><span>Click Here</span><i><svg width="16" height="16" viewBox="0 0 16 16"><circle cx="8" cy="8" r="8" fill="#fff"/><path d="M6 4.5l5 3.5-5 3.5z" fill="#333"/></svg></i></div>
  </div>
  <div class="abs dots"><b class="on"></b><b></b><b></b><b></b></div>
</section>

<section class="abs welcome">
  <h2 class="h-title">
    <svg width="24" height="26" viewBox="0 0 24 26"><path d="M2 16l5 7L22 2 8 17z" fill="#ccc"/></svg>
    Welcome to <em>TrulaPay</em>
  </h2>
  <p class="lead">TrulaPay is a direct ACH (eCheck) payment processor and online payment platform for software developers and merchants.</p>
  <p>Merchants can utilize TrulaPay's online system to initiate debits to customer accounts and view detailed transaction reports of all payment activity, in real-time. TrulaPay allows merchants to; initiate one-time payments through an online virtual terminal, setup customers for recurring payments, accept payments at the point-of-sale, and build hosted online payment forms for their website.</p>
  <p>Software developers can integrate TrulaPay's payment solution directly into their application or website utilizing TrulaPay's Payment API. Our payment API is fully documented online and available in all programming languages. TrulaPay protects developers and software from the scope of PCI Compliance by storing all sensitive payment and customer information in a PCI DSS Level 1 compliant vault.</p>
  <div class="more" style="margin-top:6px">Read More <svg width="12" height="12" viewBox="0 0 12 12"><circle cx="6" cy="6" r="6" fill="#444"/><path d="M3 6h5M6 3.5L8.5 6 6 8.5" stroke="#fff" stroke-width="1.4" fill="none"/></svg></div>
</section>

<section class="abs industries">
  <h2 class="h-title">
    <svg width="24" height="26" viewBox="0 0 24 26"><path d="M2 16l5 7L22 2 8 17z" fill="#ccc"/></svg>
    Custom Industry <em>Solutions</em>
  </h2>
  <ul>
    <li>Custom Industry Solutions</li>
    <li>Government</li>
    <li class="active">Medical</li>
    <li>Fitness</li>
    <li>Martial Arts</li>
    <li>Alarm Monitoring</li>
    <li>Property Management</li>
  </ul>
</section>

<section>
  <div class="abs band"></div>
  <h2 class="abs band-title">ACH Payment <em>Processing</em></h2>
  <article class="abs card" style="left:116px">
    <div class="photo" role="img" aria-label="Photo of a payment card lying beside a computer mouse" style="background:linear-gradient(135deg,#c9d7ec,#eef3fa 60%,#9fb4d6)"></div>
    <h3>Payment Gateway</h3>
    <p>Lorem ipsum dolor sit amet, consectw adipisicing elit, sed do eiusmod tempor incididunt ut la dolore magna aliqua. Ut enim ad minim veniam</p>
    <div class="more">Read More <svg width="12" height="12" viewBox="0 0 12 12"><circle cx="6" cy="6" r="6" fill="#444"/><path d="M3 6h5M6 3.5L8.5 6 6 8.5" stroke="#fff" stroke-width="1.4" fill="none"/></svg></div>
  </article>
  <article class="abs card" style="left:372px">
    <div class="photo" role="img" aria-label="Photo of a woman working at a laptop in a bright office" style="background:linear-gradient(135deg,#b7bcc0,#e6e3df 55%,#4a4a4a)"></div>
    <h3>ACH Payment API</h3>
    <p>Lorem ipsum dolor sit amet, consectw adipisicing elit, sed do eiusmod tempor incididunt ut la dolore magna aliqua. Ut enim ad minim veniam</p>
    <div class="more">Read More <svg width="12" height="12" viewBox="0 0 12 12"><circle cx="6" cy="6" r="6" fill="#444"/><path d="M3 6h5M6 3.5L8.5 6 6 8.5" stroke="#fff" stroke-width="1.4" fill="none"/></svg></div>
  </article>
  <article class="abs card" style="left:630px">
    <div class="photo" role="img" aria-label="Photo of three colleagues looking at a laptop together" style="background:linear-gradient(135deg,#cfd3d6,#e9dccf 50%,#bfc7cc)"></div>
    <h3>Processing for Software Development</h3>
    <p>Lorem ipsum dolor sit amet, consectw adipisicing elit, sed do eiusmod tempor incididunt ut la dolore magna aliqua. Ut enim ad minim veniam</p>
    <div class="more">Read More <svg width="12" height="12" viewBox="0 0 12 12"><circle cx="6" cy="6" r="6" fill="#444"/><path d="M3 6h5M6 3.5L8.5 6 6 8.5" stroke="#fff" stroke-width="1.4" fill="none"/></svg></div>
  </article>
</section>

<footer class="site-footer">
  <div class="abs footer"></div>
  <div class="abs foot-nav">Home<span>|</span>Solutions<span>|</span>Developers<span>|</span>Partners<span>|</span>Company<span>|</span>Resources<span>|</span>Blog</div>
  <svg class="abs" style="left:116px;top:1123px" width="13" height="17" viewBox="0 0 13 17"><path d="M6.5 0A6 6 0 0 0 .5 6c0 4.5 6 11 6 11s6-6.5 6-11a6 6 0 0 0-6-6z" fill="#ccc"/><circle cx="6.5" cy="6" r="2.3" fill="#343434"/></svg>
  <div class="abs addr" style="left:139px"><b>Marlow Ridge</b>12A Fenmore Square<br>Marlow Ridge, GA 30599</div>
  <div class="abs addr" style="left:257px"><b>Hallowfield</b>1848 Lantern Court<br>Suite C Hallowfield, GA 30398</div>
  <svg class="abs" style="left:403px;top:1124px" width="12" height="16" viewBox="0 0 12 16"><path d="M2 0l3 3.5-1.5 2c.8 2 2 3.5 3.5 4.5L9 8.5l3 3-1.5 3C5 14 0 7 0 1.5z" fill="#ddd"/></svg>
  <div class="abs addr" style="left:424px;top:1123px"><b>555-013-4477</b></div>
  <div class="abs" style="left:510px;top:1120px;font:700 17px Arial,sans-serif;color:#ddd">@</div>
  <div class="abs addr" style="left:534px;top:1123px"><b>support@trulapay.example</b></div>
  <div class="abs foot-brand">TrulaPay</div>
  <div class="abs follow">Follow Us <i style="background:#3b5b9a"></i><i style="background:#2fa8e0"></i><i style="background:#1a7bb5"></i></div>
  <div class="abs copy">© 2013. TrulaPay. All rights reserved.</div>
</footer>

</body>
</html>
```